Tech business card design

We need an amazing business card design for our new business 'Brakka' a marketing tech startup based in Sydney, Australia. We provide an online marketplace for businesses to search and buy advertising media, connect with service providers and learn more about marketing. We wish to communicate 'cool tech', reliability and professionalism and design based around our logo.

Target Market(s)

Business Owners

Contact Information for Business Card

Name
Position
Email Address
Website
Phone Number

Font styles to use
Other font styles liked:
• Avenir & Avenir Next

Colors

Designer to choose colors to be used in the design.

```html
<!DOCTYPE html>
<html lang="en">
<head>
<meta charset="utf-8">
<title>Brakka — Business Card</title>
<link rel="stylesheet" href="https://fonts.googleapis.com/css2?family=Mulish:wght@300;400;800;900&display=swap">
<style>
  :root {
    --page-bg: #ffffff;
    --navy: #15153f;
    --navy-band: #263b8e;
    --brand-blue: #1d4aa3;
    --ice-light: #eaf7fd;
    --ice-mid: #bfe6f8;
    --ice-deep: #9fd6f2;
    --arc-navy: #242a6a;
    --white: #ffffff;
    --soft-white: #dfe3f2;
  }
  * { margin: 0; padding: 0; box-sizing: border-box; }
  html, body {
    width: 1200px; height: 1000px; overflow: hidden;
    background: var(--page-bg);
    font-family: "Mulish", "Avenir Next", sans-serif;
  }
  .canvas {
    width: 1200px; height: 1000px;
    display: flex; align-items: center; justify-content: center; gap: 40px;
  }
  .card {
    position: relative;
    width: 520px; height: 290px;
    overflow: hidden;
    box-shadow: 0 6px 18px rgba(0,0,0,0.28);
  }

  /* Front */
  .card--front .front-artwork {
    position: absolute; inset: 0;
    background: radial-gradient(circle at 40% 55%, var(--ice-light) 0%, var(--ice-mid) 45%, var(--ice-deep) 100%);
  }
  .card--front .wordmark {
    position: absolute; left: 0; right: 0; top: 50%;
    transform: translateY(-50%);
    text-align: center;
    font-weight: 900; font-size: 104px; letter-spacing: -2px;
    color: var(--brand-blue);
    line-height: 1;
  }

  /* Back */
  .card--back { background: var(--navy); }
  .back-artwork {
    position: absolute; left: 0; top: 0; width: 290px; height: 278px;
    background: radial-gradient(circle at 95% 65%, var(--arc-navy) 0%, rgba(36,42,106,0.5) 45%, var(--navy) 80%);
  }
  .back-logo {
    position: absolute; left: 30px; top: 112px;
    font-weight: 900; font-size: 62px; letter-spacing: -1px;
    color: var(--white); line-height: 1;
  }
  .divider {
    position: absolute; left: 296px; top: 26px;
    width: 2px; height: 228px; background: var(--white);
  }
  .contact-block {
    position: absolute; left: 330px; top: 64px; width: 170px;
    color: var(--white);
  }
  .person-name {
    font-weight: 300; font-size: 19px; text-align: right;
  }
  .person-title {
    font-weight: 800; font-size: 15px; text-align: right;
    letter-spacing: 0.5px;
    padding-bottom: 4px;
    border-bottom: 2px solid var(--white);
    margin-left: 56px;
    margin-top: 1px;
  }
  .contact-list { list-style: none; margin-top: 20px; }
  .contact-list li {
    display: flex; align-items: center; gap: 10px;
    font-size: 9.5px; font-weight: 400; color: var(--soft-white);
    margin-bottom: 11px;
  }
  .contact-list svg { width: 13px; height: 13px; flex: none; }
  .bottom-band {
    position: absolute; left: 0; right: 0; bottom: 0; height: 12px;
    background: var(--navy-band);
  }
</style>
</head>
<body>
<main class="canvas">
  <section class="card card--front">
    <div class="front-artwork" role="img" aria-label="Light blue circular technology pattern background"></div>
    <div class="wordmark">brakka</div>
  </section>

  <section class="card card--back">
    <div class="back-artwork" role="img" aria-label="Dark blue concentric technology arcs"></div>
    <div class="back-logo">brakka</div>
    <div class="divider"></div>
    <div class="contact-block">
      <p class="person-name">Person's Name</p>
      <p class="person-title">TITLE</p>
      <ul class="contact-list">
        <li>
          <svg viewBox="0 0 14 14" fill="none" stroke="#fff" stroke-width="1.2"><rect x="3.5" y="0.8" width="7" height="12.4" rx="1.2"/><line x1="6" y1="11" x2="8" y2="11"/></svg>
          00 61 2 3456 7890
        </li>
        <li>
          <svg viewBox="0 0 14 14" fill="none" stroke="#fff" stroke-width="1.3"><circle cx="7" cy="7" r="2.4"/><path d="M9.4 7v1.2a1.6 1.6 0 0 0 3.2 0V7A5.6 5.6 0 1 0 10 11.8"/></svg>
          youremail@xyz.com
        </li>
        <li>
          <svg viewBox="0 0 14 14" fill="none" stroke="#fff" stroke-width="1.1"><circle cx="7" cy="7" r="5.8"/><ellipse cx="7" cy="7" rx="2.6" ry="5.8"/><line x1="1.2" y1="7" x2="12.8" y2="7"/></svg>
          yourWorkEmail@xyz.com
        </li>
      </ul>
    </div>
    <div class="bottom-band"></div>
  </section>
</main>
</body>
</html>
```